Verpackungen für Parfum-Proben
Besten Dank! Das Team ist begeistert - also bin ich es auch und wir freuen uns schon, unsere Parfum Proben in Zukunft in diesem tollen Design weitergeben zu können! Danke!
Zielgruppe
Hallo allerseits! Wir sind im Direktvertrieb in den Bereichen Parfum & Kosmetik tätig.
Aufgabenstellung
Für unsere Parfum-Proben benötige ich ein ansprechendes, modernes Design.
Das Design muss relativ neutral gehalten werden, da die Blister sowohl für Herren- als auch Damenproben verwendet werden.
Auf Vorder- und Rückseite soll unser Team-Logo (RuchKontor®) sichtbar sein (Vorderseite größer, Rückseite kleiner).
Auf der linken Innenseite sollte Plätz für einen netten Spruch (den ich mir noch überlege) sein.
Auf der Rückseite muss Platz (weißes / helles Feld) für einen Stempel und/oder Aufkleber (Kontaktdaten des Distributors) sein.
Unser Logo ist Lila - Das farbliche Design sollte dazu passen.
Bei Fragen, einfach Nachricht :)
Daten:
Endformat: 133 x 74 mm
Datenformat: 139 x 80 mm
1-teilig, gestanzt, genutet, einseitig geklebt geliefert
Bitte verwenden Sie für positive Schriftstärken mindestens 9pt (ca. 3,17mm) und bei negativen Schriftstärken mindestens 13pt (ca. 4,59mm).
Abmessungen / Druck- / Designvorlage, Logo, etc.: https://dateiwolke.example/ordner/X7KPtrWQ#m4vbeLhNcyrGzzt9_k2w8p

```html
<!DOCTYPE html>
<html lang="de">
<head>
<meta charset="utf-8">
<title>RuchKontor – Probenverpackung</title>
<link rel="stylesheet" href="https://fonts.googleapis.com/css2?family=Cormorant+Garamond:wght@500&family=Great+Vibes&family=Montserrat:wght@500;700&display=swap">
<style>
  :root {
    --bg: #f3f3f5;
    --purple: #3d1f78;
    --purple-deep: #2c1560;
    --purple-light: #5a3f8e;
    --photo-top: #4a3473;
    --photo-bottom: #6a5496;
    --field: #dcdcdc;
    --white: #ffffff;
    --ink: #1d1d1d;
  }
  * { margin: 0; padding: 0; box-sizing: border-box; }
  html, body { width: 1200px; height: 800px; overflow: hidden; background: var(--bg); }
  .sheet { position: relative; width: 1200px; height: 800px; }

  .panel {
    position: absolute; top: 140px; width: 340px; height: 500px;
    background: var(--purple); overflow: hidden;
  }
  .panel--front { left: 50px; }
  .panel--inside { left: 430px; background: linear-gradient(90deg, var(--purple-deep), var(--purple-light)); }
  .panel--back { left: 810px; }

  .front-photo {
    position: absolute; inset: 0;
    background: linear-gradient(160deg, var(--photo-top), var(--photo-bottom));
  }
  .logo-frame {
    position: absolute; left: 60px; top: 300px; width: 220px; height: 150px;
    border: 2px solid var(--white);
    display: flex; flex-direction: column; align-items: center; justify-content: center; gap: 14px;
  }
  .brand-name {
    font-family: "Cormorant Garamond", serif; font-weight: 500; color: var(--white);
    font-size: 34px; letter-spacing: 1px;
    display: flex; align-items: center; gap: 8px;
  }
  .brand-dot { width: 14px; height: 14px; border-radius: 50%; background: var(--white); }
  .tagline { font-family: "Great Vibes", cursive; color: var(--white); font-size: 30px; }

  .vial-holder {
    position: absolute; left: 30px; top: 40px; width: 90px; height: 420px;
  }
  .strap {
    position: absolute; left: 0; width: 90px; height: 56px;
    background: var(--purple-deep); border: 1px solid var(--purple-light);
  }
  .inside-tagline {
    position: absolute; left: 150px; top: 230px; width: 180px; text-align: center;
    font-family: "Great Vibes", cursive; color: var(--white); font-size: 30px; line-height: 1.2;
  }

  .stamp-field {
    position: absolute; left: 40px; top: 60px; width: 260px; height: 380px;
    background: var(--field); border: 6px solid #eeeeee;
    display: flex; flex-direction: column; align-items: center; padding-top: 50px; gap: 40px;
  }
  .back-copy {
    font-family: "Montserrat", sans-serif; color: var(--ink); text-align: center;
    font-size: 11px; line-height: 1.5; letter-spacing: 0.5px;
  }
  .back-copy strong { font-weight: 700; display: block; font-size: 12px; }
  .brand-name--small { color: var(--ink); font-size: 26px; }
  .brand-name--small .brand-dot { background: var(--ink); width: 11px; height: 11px; }
  .sticker-area { width: 200px; height: 150px; background: #e6e6e6; }
</style>
</head>
<body>
<main class="sheet">

  <section class="panel panel--front" aria-label="Vorderseite">
    <div class="front-photo" role="img" aria-label="Violett eingefärbtes Paarfoto: bärtiger Mann und blonde Frau"></div>
    <div class="logo-frame">
      <div class="brand-name"><span class="brand-dot"></span>RuchKontor</div>
      <div class="tagline">Finde deinen Duft</div>
    </div>
  </section>

  <section class="panel panel--inside" aria-label="Innenseite mit Probenhalter">
    <div class="vial-holder">
      <svg width="90" height="420" viewBox="0 0 90 420" aria-label="Probenfläschchen">
        <rect x="28" y="10" width="34" height="380" rx="10" fill="#f6f6f8" stroke="#cfcfd6"/>
        <rect x="26" y="0" width="38" height="34" rx="6" fill="#3d1f78"/>
        <rect x="26" y="38" width="38" height="30" rx="4" fill="#2c1560"/>
        <rect x="30" y="90" width="30" height="240" fill="#ffffff"/>
        <text x="45" y="210" transform="rotate(90 45 210)" text-anchor="middle"
              font-family="Cormorant Garamond, serif" font-size="20" fill="#3d1f78">RuchKontor</text>
      </svg>
      <div class="strap" style="top:120px"></div>
      <div class="strap" style="top:300px"></div>
    </div>
    <p class="inside-tagline">Finde deinen Duft</p>
  </section>

  <section class="panel panel--back" aria-label="Rückseite">
    <div class="stamp-field">
      <p class="back-copy"><strong>LOREM IPSUM DOLOR SIT AMET</strong>CONSECTETUER ADIPISCING ELIT, SED DIAM<br>NONUMMY</p>
      <div class="brand-name brand-name--small"><span class="brand-dot"></span>RuchKontor</div>
      <div class="sticker-area" aria-label="Feld für Stempel oder Aufkleber"></div>
    </div>
  </section>

</main>
</body>
</html>
```